Homecare Information Flyer

We require a brochure/ leaflet to be created which would provide healthcare information to our staff and patients on the topic of- Pressure Ulcers. The document would ideally be 3 fold. It should include our Logo/ Company Information (Marrowby Staffing).

I have attached-
- Logo
- Text/ Visual images to be included.

Industry/Entity Type

Healthcare

```html
<!DOCTYPE html>
<html lang="en">
<head>
<meta charset="utf-8">
<title>Pressure Area Care – A Guide For Patients</title>
<link rel="stylesheet" href="https://fonts.googleapis.com/css2?family=Archivo+Black&family=Arimo:wght@400;700&display=swap">
<style>
  :root {
    --green: #7aa92e;
    --green-dark: #4f7d16;
    --grey: #6b6b6b;
    --grey-text: #555555;
    --body-text: #4a4a4a;
    --white: #ffffff;
    --photo-warm: #e9dccd;
    --photo-cool: #cfd8dc;
  }
  * { box-sizing: border-box; margin: 0; padding: 0; }
  html, body { width: 1200px; height: 849px; overflow: hidden; background: var(--white); }
  body { font-family: "Arimo", Arial, sans-serif; color: var(--body-text); }

  .leaflet { position: relative; width: 1200px; height: 849px; }
  .panel { position: absolute; width: 400px; }
  .inside-left  { left: 0;   top: 0; height: 603px; }
  .inside-mid   { left: 400px; top: 0; height: 603px; }
  .cover        { left: 800px; top: 0; height: 603px; }
  .back-left    { left: 0;   top: 616px; height: 233px; background: var(--green); }
  .back-mid     { left: 400px; top: 616px; height: 233px; }
  .back-right   { left: 800px; top: 616px; height: 233px; background: var(--green); }

  .fold-band { position: absolute; top: 603px; height: 13px; width: 400px; }
  .fold-band.grey { background: var(--grey); }
  .fold-band.green { background: var(--green); }

  /* Inside left */
  .hero-photo {
    position: absolute; left: 0; top: 0; width: 400px; height: 235px;
    background: linear-gradient(180deg, #d9d4cc 0%, #ece7e1 55%, rgba(255,255,255,0) 100%),
                linear-gradient(90deg, #3d4a5c 0%, #c9c2b8 30%, #efe6da 100%);
  }
  .hero-photo::after {
    content: ""; position: absolute; inset: 0;
    background: linear-gradient(180deg, rgba(255,255,255,0) 55%, var(--white) 100%);
  }
  .section-head {
    position: absolute; left: 28px; width: 333px; height: 36px;
    background: var(--green); color: var(--white);
    font-family: "Archivo Black", "Arial Black", sans-serif; font-size: 12.5px;
    padding: 13px 0 0 12px; box-shadow: 2px 2px 0 #3a3a3a;
  }
  .copy { position: absolute; left: 40px; width: 330px; font-size: 13.2px; line-height: 14.8px; }
  .copy .term { color: var(--green); display: block; }
  .copy p + p { margin-top: 14px; }

  /* Inside middle */
  .contact {
    position: absolute; left: 0; width: 400px; top: 449px; text-align: center;
    font-family: "Archivo Black", "Arial Black", sans-serif; font-size: 12.5px; line-height: 16px;
    color: var(--grey-text);
  }
  .contact .accent { color: var(--green); }
  .contact .gap { margin-top: 16px; }

  /* Cover */
  .cover-bar { position: absolute; top: 0; left: 0; width: 360px; height: 40px; background: var(--green); }
  .cover-bar-end { position: absolute; top: 0; left: 360px; width: 40px; height: 40px; background: var(--grey); }
  .cover-photo {
    position: absolute; top: 40px; left: 0; width: 400px; height: 563px;
    background: linear-gradient(135deg, #f2efe9 0%, #e7dccf 40%, #d8cbbd 70%, #b9a89a 100%);
  }
  .cover-title {
    position: absolute; left: 42px; top: 520px; color: var(--green);
    font-family: "Archivo Black", "Arial Black", sans-serif; font-size: 28px; line-height: 30px;
    letter-spacing: -0.3px;
  }
  .cover-subtitle {
    position: absolute; left: 42px; top: 554px; color: var(--green);
    font-size: 21px; line-height: 24px;
  }

  /* Back panels */
  .testimonial {
    position: absolute; left: 40px; width: 320px; top: 60px; text-align: center;
    color: var(--white); font-size: 13.2px; line-height: 15.4px;
  }
  .testimonial h2 { font-size: 13.5px; font-weight: 700; }
  .testimonial cite { font-style: normal; font-weight: 700; display: block; }
  .team-photo {
    width: 400px; height: 233px;
    background: linear-gradient(180deg, #eef1f3 0%, #d9e2e6 45%, #8fc3d8 75%, #6fb3cf 100%);
  }
  .brand { position: absolute; left: 0; top: 48px; width: 400px; text-align: center; }
  .brand-mark { display: block; margin: 0 auto 12px; }
  .brand-name {
    font-family: "Arimo", Arial, sans-serif; font-weight: 700; font-size: 30px;
    color: var(--grey); letter-spacing: -0.5px;
  }
</style>
</head>
<body>
<main class="leaflet">

  <section class="panel inside-left">
    <div class="hero-photo" role="img" aria-label="Photo of a nurse talking with a smiling elderly patient in a bright ward"></div>

    <h2 class="section-head" style="top:180px">What is a Pressure Ulcer?</h2>
    <div class="copy" style="top:223px">
      <p>A pressure ulcer is an area of damage to the skin and underlying tissue. They are sometimes known as pressure sores or bed sores.</p>
    </div>

    <h2 class="section-head" style="top:280px">What causes a Pressure Ulcer?</h2>
    <div class="copy" style="top:323px">
      <p>Pressure ulcers are caused by poor circulation to tissues due to a combination of the following factors:</p>
      <p><span class="term">Pressure</span>Body weight and some equipment (e.g. anti-thrombosis stockings) can squash the skin and other tissues where parts are under pressure. This reduces the blood supply to the area and can lead to tissue damage.</p>
      <p><span class="term">Shearing</span>Sliding or slumping down the bed/chair can damage the skin and deeper layers of tissue.</p>
      <p><span class="term">Friction</span>Poor moving and handling methods can remove the top layers of skin. Repeated friction can increase your risk.</p>
    </div>
  </section>

  <section class="panel inside-mid">
    <address class="contact" style="font-style:normal">
      <div>Four Alder Court, Fulbrook</div>
      <div>London W9 2QT</div>
      <div class="gap">Tel <span class="accent">0204 555 0142</span></div>
      <div>Fax <span class="accent">0204 555 0143</span></div>
      <div>Email <span class="accent">hello@marrowbystaffing.co.uk</span></div>
      <div class="gap accent">www.marrowbystaffing.co.uk</div>
    </address>
  </section>

  <section class="panel cover">
    <div class="cover-bar"></div>
    <div class="cover-bar-end"></div>
    <div class="cover-photo" role="img" aria-label="Photo of a smiling doctor with a stethoscope greeting a patient"></div>
    <h1 class="cover-title">Pressure Area Care</h1>
    <p class="cover-subtitle">A Guide For Patients</p>
  </section>

  <div class="fold-band grey" style="left:0"></div>
  <div class="fold-band green" style="left:400px"></div>
  <div class="fold-band grey" style="left:800px"></div>

  <section class="panel back-left">
    <blockquote class="testimonial">
      <h2>Testimonials</h2>
      <p>"It was great working for Marrowby staffing, I was made part of the family and was very well looked after. Marrowby staffing is a wonderful agency to work for and the staff were very kind and understanding. Thank you very much"</p>
      <cite>Delia Harwood, Agency RGN, London</cite>
    </blockquote>
  </section>

  <section class="panel back-mid">
    <div class="team-photo" role="img" aria-label="Photo of a smiling team of nurses and healthcare staff in scrubs"></div>
  </section>

  <section class="panel back-right">
    <div class="brand">
      <svg class="brand-mark" width="88" height="88" viewBox="0 0 88 88" aria-hidden="true">
        <circle cx="44" cy="44" r="44" fill="var(--green-dark)"/>
      </svg>
      <span class="brand-name">Marrowby Staffing</span>
    </div>
  </section>

</main>
</body>
</html>
```